VORLEN Website Design

We need a website designed for our company VORLEN. We are a luxury lifestyle club that will provide benefits and services for our members. The site should be clean & sleek, preferably using black and white (or darker colors). (example sites: brimvale.example, tusko.example)

Here is a link of a sample page I did using wix. (https://pelmundry4.sitebuild.example/mypage) This can be used to get a general idea.

Target Market(s)

Upper Middle Class in the United States

Number of Pages Required

5+ page

Font styles to use
Sans Serif
Other font styles liked:
• Arial (or other similar fonts)

Requirements
Must have
• A clean design that is eye-catching and speaks to our company.
Nice to have
• Ideas for copy.

```html
<!DOCTYPE html>
<html lang="en">
<head>
<meta charset="utf-8">
<title>VORLEN – The Ultimate Full Service Lifestyle Club</title>
<link rel="stylesheet" href="https://fonts.googleapis.com/css2?family=Catamaran:wght@400;600;700;800&display=swap">
<style>
:root{
  --bg:#1c1c1c;
  --header:#242424;
  --dark-section:#252525;
  --white:#ffffff;
  --ink:#222222;
  --text:#333333;
  --accent:#3fa9f5;
  --accent-deep:#1386d0;
  --field:#2e2e2e;
  --footer:#262626;
  --muted:#cfcfcf;
}
*{box-sizing:border-box;margin:0;padding:0}
html,body{width:1200px;height:1200px;overflow:hidden;background:var(--bg);font-family:"Catamaran",Arial,sans-serif;color:var(--text)}
.page{position:absolute;left:306px;top:0;width:589px;height:1200px}
.abs{position:absolute}
/* header */
.site-header{left:0;top:0;width:589px;height:50px;background:linear-gradient(#2b2b2b,#1f1f1f)}
.logo{left:64px;top:10px;font-size:22px;font-weight:400;color:var(--white);letter-spacing:.5px}
.nav{top:19px;font-size:8.5px;font-weight:600;color:#b9b9b9;letter-spacing:.3px}
.nav.active{color:var(--white);border-bottom:2px solid var(--accent);padding-bottom:1px}
/* hero */
.hero{left:0;top:50px;width:589px;height:226px;background:linear-gradient(120deg,#3a3f4a 0%,#6b5a48 40%,#4a4036 65%,#2b2e36 100%)}
.hero-caption{left:0;top:188px;width:589px;height:38px;background:rgba(0,0,0,.85);color:var(--white);font-size:22px;font-weight:700;text-align:center;line-height:40px}
.hero-arrow{top:100px}
/* welcome */
.welcome{left:0;top:276px;width:589px;height:189px;background:var(--white)}
.h2{font-size:17px;font-weight:800;color:var(--ink);letter-spacing:.3px}
.h2 span{color:var(--accent)}
.welcome-photo{left:63px;top:54px;width:109px;height:94px;border-radius:4px;background:linear-gradient(160deg,#8ec9ef 0%,#3fb3c9 45%,#e6dcc4 70%,#4d6b3a 100%);box-shadow:0 1px 3px rgba(0,0,0,.3)}
.welcome-text{left:181px;top:52px;width:340px;font-size:8.6px;line-height:17.2px;color:var(--text)}
.read-more{left:488px;top:153px;font-size:7.5px;font-weight:700;color:var(--ink);border-bottom:2px solid var(--accent)}
/* store */
.store{left:0;top:465px;width:589px;height:325px;background:radial-gradient(ellipse at 50% 40%,#333 0%,#222 70%)}
.store-title{left:0;top:14px;width:589px;text-align:center;color:var(--white)}
.store-title.h2{color:var(--white)}
.card{top:52px;width:225px;height:210px;background:var(--white);border-radius:3px;overflow:hidden}
.card-photo{width:225px;height:154px}
.card h3{margin-top:7px;text-align:center;font-size:10px;font-weight:800;color:var(--accent-deep);letter-spacing:.3px}
.card p{text-align:center;font-size:7px;line-height:9px;color:#333;padding:0 5px}
.cta{left:202px;top:285px;width:183px;height:24px;border:2px solid var(--white);border-radius:4px;background:var(--accent-deep);color:var(--white);font-size:12px;font-weight:800;text-align:center;line-height:22px;letter-spacing:.3px}
/* contact */
.contact{left:0;top:790px;width:589px;height:332px;background:var(--white)}
.contact-title{left:0;top:22px;width:589px;text-align:center}
.label{font-size:10px;font-weight:800;color:var(--ink);letter-spacing:.3px}
.label span{color:var(--accent)}
.small{font-size:7.2px;line-height:12px;color:#333}
.map{left:64px;top:208px;width:225px;height:106px;border-radius:3px;background:linear-gradient(135deg,#f4efe0 0%,#eae6d6 55%,#dfe6cf 100%);box-shadow:0 1px 3px rgba(0,0,0,.3)}
.field{left:339px;width:185px;height:21px;background:var(--field);border-radius:3px;color:#e0e0e0;font-size:7.2px;padding:6px 9px}
.submit{left:460px;top:292px;width:61px;height:23px;border:2px solid #0f6fb0;border-radius:4px;background:var(--accent-deep);color:var(--white);font-size:10px;font-weight:800;text-align:center;line-height:21px;letter-spacing:.4px}
/* footer */
.footer{left:0;top:1122px;width:589px;height:78px;background:var(--footer)}
.foot-links{left:64px;top:27px;font-size:8.5px;font-weight:600;color:var(--white);letter-spacing:.2px;word-spacing:1px}
.foot-links i{font-style:normal;margin:0 9px}
.copy{left:64px;top:47px;font-size:6.8px;color:var(--muted)}
.social{top:20px;width:30px;height:31px;background:#2f2f2f}
</style>
</head>
<body>
<div class="page">
  <header class="abs site-header">
    <div class="abs logo">VORLEN</div>
    <div class="abs nav active" style="left:261px">HOME</div>
    <div class="abs nav" style="left:310px">ABOUT</div>
    <div class="abs nav" style="left:363px">SERVICES &amp; BENIFITS</div>
    <div class="abs nav" style="left:472px">CONTACT US</div>
  </header>

  <section class="abs hero" role="img" aria-label="Club members toasting with wine glasses around a dinner table">
    <svg class="abs hero-arrow" style="left:61px" width="10" height="24" viewBox="0 0 10 24"><path d="M9 1 L2 12 L9 23" fill="none" stroke="#fff" stroke-width="1.3"/></svg>
    <svg class="abs hero-arrow" style="left:516px" width="10" height="24" viewBox="0 0 10 24"><path d="M1 1 L8 12 L1 23" fill="none" stroke="#fff" stroke-width="1.3"/></svg>
    <div class="abs hero-caption">The Ultimate Full Service Lifestyle Club</div>
  </section>

  <section class="abs welcome">
    <h2 class="abs h2" style="left:64px;top:20px">WELCOME TO <span>OUR WEBSITE</span></h2>
    <div class="abs welcome-photo" role="img" aria-label="Tropical beach with turquoise water and palm trees"></div>
    <p class="abs welcome-text">VORLEN is a members only lifestyle club founded in order to bring the best services, experiences, and opportunities to our diverse community of members.<br>Our members consist of creatives, athletes, artists, and other professionals.<br>VORLEN was formed to bring the best services, experiences, and exclusive opportunities to our members. With everything from private member events to private jet travel, the perks of being a VORLEN member are unmatched.</p>
    <div class="abs read-more">READ MORE</div>
  </section>

  <section class="abs store">
    <h2 class="abs h2 store-title">WHAT’S IN STORE FOR YOU AT <span>VORLEN</span></h2>
    <article class="abs card" style="left:64px">
      <div class="card-photo" role="img" aria-label="Members stepping off a private jet onto a red carpet" style="background:linear-gradient(180deg,#9cc3e6 0%,#e8eef2 45%,#6e7378 70%,#c7494a 100%)"></div>
      <h3>SERVICES AND BENEFITS</h3>
      <p>VORLEN membership provides you with amazing benefits and services. Members receive access to the best accountants, attorneys, real estate agents, private bankers/advisers and more...</p>
    </article>
    <article class="abs card" style="left:299px">
      <div class="card-photo" role="img" aria-label="Diver swimming beside a manta ray over a coral reef" style="background:linear-gradient(180deg,#3da3d6 0%,#1c7fb8 50%,#0f4f7a 100%)"></div>
      <h3>EXPERIENCES</h3>
      <p>VORLEN organizes and supports a ton of private events and parties for our members.<br>Members are also provided access to exclusive venues and events from</p>
    </article>
    <div class="abs cta">BECOME A MEMBER NOW !!</div>
  </section>

  <section class="abs contact">
    <h2 class="abs h2 contact-title">CONTACT <span>US</span></h2>
    <div class="abs label" style="left:64px;top:70px">ADDRESS</div>
    <p class="abs small" style="left:64px;top:85px;width:180px">Lorem Ipsum is simply dummy text of the printing and typesetting industry. Lorem Ipsum has been the industry's standard dummy text ever since the 1500s,</p>
    <div class="abs label" style="left:64px;top:130px">EMAIL</div>
    <p class="abs small" style="left:64px;top:144px">info@vorlen.example</p>
    <div class="abs label" style="left:64px;top:170px">WEBSITE</div>
    <p class="abs small" style="left:64px;top:185px">www.vorlen.example</p>
    <div class="abs map" role="img" aria-label="Road map showing the club's location"></div>

    <div class="abs label" style="left:339px;top:70px">WE’RE ALWAYS HERE, <span>DROP US A LINE!</span></div>
    <div class="abs field" style="top:100px">Name</div>
    <div class="abs field" style="top:130px">Email</div>
    <div class="abs field" style="top:160px">Subject</div>
    <div class="abs field" style="top:189px;height:88px">Message</div>
    <div class="abs submit">SUBMIT</div>
  </section>

  <footer class="abs footer">
    <div class="abs foot-links">HOME<i>I</i>ABOUT US<i>I</i>SERVICES &amp; BENEFITS<i>I</i>CONTACT US</div>
    <div class="abs copy">COPYRIGHTS 2018. ALL RIGHTS RESERVED.</div>
    <div class="abs social" style="left:404px"><svg width="30" height="31"><circle cx="15" cy="15.5" r="10" fill="none" stroke="#888" stroke-width="1"/></svg></div>
    <div class="abs social" style="left:434px"><svg width="30" height="31"><circle cx="15" cy="15.5" r="10" fill="none" stroke="#888" stroke-width="1"/></svg></div>
    <div class="abs social" style="left:464px"><svg width="30" height="31"><circle cx="15" cy="15.5" r="10" fill="none" stroke="#888" stroke-width="1"/></svg></div>
    <div class="abs social" style="left:494px"><svg width="30" height="31"><circle cx="15" cy="15.5" r="10" fill="none" stroke="#888" stroke-width="1"/></svg></div>
  </footer>
</div>
</body>
</html>
```